Statonary for Design Build Firm
Design Build company
Statonary for Design Build Firm -
Creative Brief
Professional
Peter L. Vondrasek
C.E.O.
Dubai UAE
US# 1-415-372-9054
mvelondrask@tmwrgroup.net
www.tmwrgroup.net

```html
<!DOCTYPE html>
<html lang="en">
<head>
<meta charset="utf-8">
<title>TMWR Group – Business Card</title>
<link rel="stylesheet" href="https://fonts.googleapis.com/css2?family=Montserrat:wght@400;600;800&display=swap">
<style>
  :root {
    --page: #ffffff;
    --card: #ffffff;
    --card-edge: #2c2c2c;
    --ink: #1e1e1e;
    --muted: #8a8a8a;
    --accent: #e8821e;
    --blue-deep: #0b2f6b;
    --blue-mid: #1457a8;
    --blue-light: #3f86d6;
    --sheen: #e6e9ee;
  }
  * { margin: 0; padding: 0; box-sizing: border-box; }
  html, body {
    width: 1200px; height: 857px; overflow: hidden;
    background: var(--page);
    font-family: "Montserrat", Arial, sans-serif;
  }
  .business-card {
    position: absolute;
    left: 329px; top: 235px;
    width: 602px; height: 346px;
    background: var(--card);
    border: 2px solid var(--card-edge);
    box-shadow: 2px 3px 6px rgba(0,0,0,0.25);
    overflow: hidden;
  }
  .card-art { position: absolute; inset: 0; width: 100%; height: 100%; }
  .brand {
    position: absolute; left: 22px; top: 42px;
    display: flex; align-items: center; gap: 22px;
  }
  .brand-square {
    width: 68px; height: 68px;
    background: var(--blue-mid);
    transform: rotate(45deg);
    margin: 14px;
  }
  .brand-name {
    font-size: 27px; font-weight: 800; color: var(--blue-deep);
    letter-spacing: 0.5px; white-space: nowrap;
  }
  .location {
    position: absolute; left: 389px; top: 83px;
    font-size: 21px; font-weight: 400; color: var(--accent);
    white-space: nowrap;
  }
  .person { position: absolute; left: 30px; top: 203px; width: 215px; text-align: center; }
  .person-name { font-size: 17px; font-weight: 800; color: var(--ink); white-space: nowrap; }
  .person-title { font-size: 10px; font-weight: 600; color: var(--ink); margin-top: 6px; }
  .contact { position: absolute; left: 290px; top: 200px; list-style: none; }
  .contact li {
    font-size: 13px; color: var(--ink); line-height: 24px;
    letter-spacing: -0.2px; white-space: nowrap;
  }
  .contact-label { color: var(--accent); font-weight: 800; margin-right: 3px; }
  .website {
    position: absolute; left: 55px; top: 306px;
    font-size: 13px; color: var(--muted);
    letter-spacing: 10px; white-space: nowrap;
  }
</style>
</head>
<body>
  <section class="business-card">
    <svg class="card-art" viewBox="0 0 602 346" aria-hidden="true">
      <defs>
        <linearGradient id="chevronFill" x1="0" y1="0" x2="1" y2="1">
          <stop offset="0" stop-color="var(--blue-light)"/>
          <stop offset="0.5" stop-color="var(--blue-mid)"/>
          <stop offset="1" stop-color="var(--blue-deep)"/>
        </linearGradient>
      </defs>
      <polygon points="516,0 602,0 602,346 446,346 566,170" fill="var(--sheen)"/>
      <polygon points="530,0 602,0 602,346 460,346 580,170" fill="url(#chevronFill)"/>
    </svg>

    <div class="brand">
      <span class="brand-square"></span>
      <span class="brand-name">TMWR GROUP</span>
    </div>

    <p class="location">Dubai UAE</p>

    <div class="person">
      <p class="person-name">Peter L. Vondrasek</p>
      <p class="person-title">C.E.O.</p>
    </div>

    <ul class="contact">
      <li><span class="contact-label">P</span>US# 1-415-372-9054</li>
      <li><span class="contact-label">C</span>+971 (0)50 827 3316</li>
      <li><span class="contact-label">E</span>mvelondrask@tmwrgroup.net</li>
    </ul>

    <p class="website">www.tmwrgroup.net</p>
  </section>
</body>
</html>
```